Tavenorix - world unique technology for better life - please let them know who am i at first sight

We need a new business card for company which is a provider of unique crystal based technology suitable for all living being. For more information and final design you can use our brochure (our colours are black and blue from brochure).
We use Verdana font

Industry/Entity Type

Business

Contact Information for Business Card

regular dimension

Font styles to use
Other font styles liked:
• Verdana

Requirements
Must have
• Logo
• name
• function/position
• phone
• mobile
• e-mail
• adress
Nice to have
• inovative design (technology directed)

```html
<!DOCTYPE html>
<html lang="en">
<head>
<meta charset="utf-8">
<title>Tavenorix Business Card</title>
<link rel="stylesheet" href="https://fonts.googleapis.com/css2?family=Open+Sans:ital,wght@0,400;0,600;0,700;1,700&display=swap">
<style>
  :root {
    --backdrop: #d8c89c;
    --card-black: #050505;
    --brand-blue: #1ea9e1;
    --band-blue: #21a6dc;
    --halo: #14232c;
    --text-white: #ffffff;
    --rule-silver: #c9ced2;
  }
  * { margin: 0; padding: 0; box-sizing: border-box; }
  html, body {
    width: 1200px; height: 978px; overflow: hidden;
    background: var(--backdrop);
    font-family: 'Open Sans', Verdana, sans-serif;
  }
  .stage {
    width: 1200px; height: 978px;
    display: flex; flex-direction: column; align-items: center; justify-content: center; gap: 56px;
  }
  .card {
    position: relative; width: 700px; height: 400px;
    border-radius: 26px; overflow: hidden;
    background: var(--card-black);
    box-shadow: 0 10px 24px rgba(0,0,0,.25);
  }
  /* back side */
  .card-back .halo {
    position: absolute; left: 190px; top: 30px;
    width: 300px; height: 300px; border-radius: 50%;
    background: var(--halo);
  }
  .card-back .brand-name {
    position: absolute; left: 0; right: 0; top: 118px; text-align: center;
    color: var(--brand-blue); font-size: 84px; font-weight: 400; letter-spacing: 2px;
  }
  .card-back .website {
    position: absolute; left: 0; right: 0; top: 318px; text-align: center;
    color: var(--text-white); font-size: 19px; font-weight: 700; letter-spacing: 2px;
  }
  /* front side */
  .card-front .band { position: absolute; inset: 0; width: 700px; height: 400px; }
  .card-front .logo {
    position: absolute; left: 150px; top: 30px; display: flex; align-items: center; gap: 18px;
  }
  .card-front .logo-dot {
    width: 62px; height: 62px; border-radius: 50%; background: var(--brand-blue);
  }
  .card-front .logo-name {
    color: var(--brand-blue); font-size: 50px; font-weight: 400; letter-spacing: 1.5px;
  }
  .identity {
    position: absolute; left: 150px; top: 112px;
    color: var(--text-white); font-size: 19px; line-height: 1.3;
  }
  .identity .person { color: var(--brand-blue); font-weight: 700; font-style: italic; font-size: 22px; }
  .contacts {
    position: absolute; left: 58px; top: 204px;
    color: var(--text-white); font-size: 16px; line-height: 1;
  }
  .contact-row { display: flex; gap: 26px; margin-bottom: 12px; }
  .contact-item { display: flex; align-items: center; gap: 7px; }
  .contact-item svg { width: 16px; height: 16px; fill: none; stroke: var(--text-white); stroke-width: 1.6; }
</style>
</head>
<body>
<main class="stage">
  <section class="card card-back" aria-label="Card back">
    <div class="halo"></div>
    <div class="brand-name">TAVENORIX</div>
    <div class="website">www.tavenorix.cu</div>
  </section>

  <section class="card card-front" aria-label="Card front">
    <svg class="band" viewBox="0 0 700 400" preserveAspectRatio="none">
      <path d="M0,168 C300,172 480,190 700,360 L700,400 L0,400 Z" fill="var(--band-blue)"/>
      <path d="M0,156 C300,160 480,178 700,348" fill="none" stroke="var(--rule-silver)" stroke-width="4"/>
    </svg>
    <div class="logo">
      <div class="logo-dot"></div>
      <div class="logo-name">TAVENORIX</div>
    </div>
    <p class="identity"><span class="person">Mirela Kostanjevac,</span> Founder and CEO</p>
    <div class="contacts">
      <div class="contact-row">
        <span class="contact-item">
          <svg viewBox="0 0 16 16"><path d="M3 2h3l1.5 3.5-2 1.2a8 8 0 0 0 3.8 3.8l1.2-2L14 10v3a1 1 0 0 1-1 1A11 11 0 0 1 2 3a1 1 0 0 1 1-1z"/></svg>
          014-275-3906
        </span>
        <span class="contact-item">
          <svg viewBox="0 0 16 16"><rect x="4" y="1.5" width="8" height="13" rx="1.5"/><path d="M7 12.2h2"/></svg>
          014-275-3906
        </span>
      </div>
      <div class="contact-row">
        <span class="contact-item">
          <svg viewBox="0 0 16 16"><rect x="1.5" y="3.5" width="13" height="9" rx="1"/><path d="M1.5 4l6.5 5 6.5-5"/></svg>
          info@tavenorix.com
        </span>
        <span class="contact-item">
          <svg viewBox="0 0 16 16"><circle cx="8" cy="8" r="6.5"/><path d="M1.5 8h13M8 1.5c-3 3.5-3 9.5 0 13M8 1.5c3 3.5 3 9.5 0 13"/></svg>
          www.tavenorix.cu
        </span>
      </div>
      <div class="contact-row">
        <span class="contact-item">Street Name, City Name, Zipcode-01234</span>
      </div>
    </div>
  </section>
</main>
</body>
</html>
```